Packaging design coffee brand

Creating a packaging design for coffee products. an existing brand shall be repositioned, complete redesign. capsules, beans, etc. We need a label for the coffee whole bean package, a folded packaging for coffee capsules, see attachment. The package for the whole bean also shall be changed into a full printed packaging.

The logo is already created, but you can play with the elements, the position of symbol and name.

Target Market(s)

Europe

Industry/Entity Type

coffee

Font styles to use
Sans Serif

Requirements
Must have
• we already have a logo, which shall be used. Position of the symbol and name can be adjusted.
Nice to have
• please see the briefing attached, there you find al relevant information.
Should not have
• shall not be ecological, it shal be a lifestyle brand.

```html
<!DOCTYPE html>
<html lang="en">
<head>
<meta charset="utf-8">
<title>Orvela – Whole Bean Coffee Packaging</title>
<link href="https://fonts.googleapis.com/css2?family=Ubuntu:wght@400;500&family=Roboto+Condensed:wght@400;700;900&display=swap" rel="stylesheet">
<style>
  :root {
    --backdrop: #e6e7e7;
    --pack: #2a2d30;
    --ink-light: #d3d8d9;
    --rule: #8d9396;
    --curve-line: #5b6164;
    --label-box: #c5cccd;
    --bean-dark: #3b1c12;
    --bean-mid: #7a3a22;
    --bean-light: #a85a38;
  }
  * { box-sizing: border-box; margin: 0; padding: 0; }
  html, body { width: 845px; height: 1200px; overflow: hidden; }
  body { background: var(--backdrop); font-family: "Ubuntu", sans-serif; color: var(--ink-light); position: relative; }

  .panel-slot { position: absolute; top: 296px; width: 380px; height: 608px; }
  .panel-slot.front { left: 28px; }
  .panel-slot.back { left: 437px; }
  .panel {
    position: absolute; top: 0; left: 0; width: 400px; height: 640px;
    transform: scale(0.95); transform-origin: top left;
    background: var(--pack); overflow: hidden;
    box-shadow: 6px 8px 14px rgba(0,0,0,0.35);
  }
  .panel-art { position: absolute; inset: 0; width: 400px; height: 640px; }

  .brand-mark { position: absolute; left: 0; width: 100%; display: flex; flex-direction: column; align-items: center; }
  .brand-dot { width: 70px; height: 70px; border-radius: 50%; background: var(--ink-light); }
  .brand-name { font-size: 36px; font-weight: 400; letter-spacing: 2px; line-height: 1; }
  .front .brand-mark { top: 204px; }
  .front .brand-name { margin-top: 20px; }
  .back .brand-mark { top: 160px; }
  .back .brand-name { margin-top: 6px; }
  .product-type { position: absolute; top: 344px; width: 100%; text-align: center; font-size: 15px; letter-spacing: 0.3px; }

  .claims { position: absolute; left: 62px; top: 408px; width: 142px; font-size: 13px; line-height: 17px; }
  .claims p { border-top: 1.5px solid var(--rule); padding: 4px 0 3px; }
  .claims p:last-child { border-bottom: 1.5px solid var(--rule); }
  .net-weight { position: absolute; left: 63px; top: 579px; font-size: 12.5px; line-height: 16px; }

  .story { position: absolute; left: 30px; top: 282px; width: 187px; font-size: 11px; line-height: 14.7px; text-align: justify; text-align-last: center; hyphens: manual; }
  .note { position: absolute; left: 32px; top: 534px; width: 180px; font-size: 11px; line-height: 14px; }
  .label-space { position: absolute; left: 240px; top: 526px; width: 128px; height: 56px; background: var(--label-box); }

  .nutrition { position: absolute; left: 226px; top: 284px; width: 142px; border: 1px solid var(--ink-light); padding: 2px 3px; font-family: "Roboto Condensed", sans-serif; font-size: 6.3px; line-height: 9.9px; }
  .nutrition h3 { font-size: 16px; font-weight: 900; line-height: 17px; border-bottom: 1px solid var(--ink-light); }
  .nutrition .row { display: flex; justify-content: space-between; border-bottom: 0.5px solid var(--rule); }
  .nutrition .thick { border-bottom: 4px solid var(--ink-light); font-weight: 700; font-size: 8px; }
  .nutrition .calories { font-size: 13px; font-weight: 900; line-height: 16px; border-bottom: 2.5px solid var(--ink-light); align-items: flex-end; }
  .nutrition .calories span:last-child { font-size: 16px; }
  .nutrition .small { font-size: 5px; line-height: 7px; border: none; }
  .nutrition .dv { justify-content: flex-end; font-weight: 700; font-size: 5px; }
  .nutrition b { font-weight: 700; }
  .nutrition .in1 { padding-left: 8px; }
  .nutrition .in2 { padding-left: 17px; }
  .nutrition .row:last-child { border-bottom: none; }
</style>
</head>
<body>

<section class="panel-slot front">
  <div class="panel">
    <svg class="panel-art" viewBox="0 0 400 640">
      <defs>
        <linearGradient id="beanTone" x1="0" y1="0" x2="1" y2="1">
          <stop offset="0" stop-color="var(--bean-light)"/>
          <stop offset="0.5" stop-color="var(--bean-mid)"/>
          <stop offset="1" stop-color="var(--bean-dark)"/>
        </linearGradient>
      </defs>
      <path d="M400 340 C375 338 355 350 352 375 C348 405 345 430 315 445 C285 460 245 460 215 480 C170 510 130 560 110 640" fill="none" stroke="var(--curve-line)" stroke-width="3"/>
      <path role="img" aria-label="Photo of roasted coffee beans" fill="url(#beanTone)"
            d="M400 355 C385 352 370 360 368 380 C365 410 360 440 330 455 C300 470 260 470 230 490 C190 515 150 550 128 640 L400 640 Z"/>
    </svg>
    <div class="brand-mark">
      <span class="brand-dot"></span>
      <span class="brand-name">ORVELA</span>
    </div>
    <p class="product-type">WHOLE BEAN COFFEE</p>
    <div class="claims">
      <p>100% Arabica Blend.</p>
      <p>Organic and Fair<br>Trade Certified</p>
    </div>
    <p class="net-weight">12OZ<br>(340g)</p>
  </div>
</section>

<section class="panel-slot back">
  <div class="panel">
    <div class="brand-mark">
      <span class="brand-dot"></span>
      <span class="brand-name">ORVELA</span>
    </div>
    <p class="story">Lorem ipsum dolor sit amet, consectetuer adipiscing elit, sed diam nonummy nibh euismod tincidunt ut laoreet dolore magna aliquam erat volutpat. Ut wisi enim ad minim veniam, quis nostrud exerci tation ullamcorp&shy;er suscipit lobortis nisl ut aliquip ex ea commodo consequat. Duis autem vel eum iriure dolor in hendre Lorem ipsum dolor sit amet, consectetuer ullamcorper suscipit lobortis nisl ut aliquip ex ea commodo consequat. Duis autem vel eum iriure dolor in hendre</p>
    <div class="nutrition">
      <h3>Nutrition Facts</h3>
      <div class="row small" style="font-size:6px;line-height:8px">10 servings per container</div>
      <div class="row thick"><span>Serving size</span><span>1 cup (55g)</span></div>
      <div class="row small" style="font-weight:700;padding-top:1px">Amount per serving</div>
      <div class="row calories"><span>Calories</span><span>165</span></div>
      <div class="row dv"><span>% Daily Value*</span></div>
      <div class="row"><span><b>Total Fat</b> 1.5g</span><b>2%</b></div>
      <div class="row in1"><span>Saturated Fat 0.5g</span><b>3%</b></div>
      <div class="row in1"><span>Trans Fat 0g</span><span></span></div>
      <div class="row in1"><span>Polyunsaturated Fat 0.5g</span><span></span></div>
      <div class="row in1"><span>Monounsaturated Fat 0.5g</span><span></span></div>
      <div class="row"><span><b>Cholesterol</b> 0mg</span><b>0%</b></div>
      <div class="row"><span><b>Sodium</b> 180mg</span><b>8%</b></div>
      <div class="row"><span><b>Fluoride</b> 0g</span><span></span></div>
      <div class="row"><span><b>Total Carbohydrate</b> 21g</span><b>8%</b></div>
      <div class="row in1"><span>Dietary Fiber 2g</span><b>7%</b></div>
      <div class="row in2"><span>Soluble Fiber &lt;1g</span><span></span></div>
      <div class="row in2"><span>Insoluble Fiber 1g</span><span></span></div>
      <div class="row in1"><span>Total Sugars 8g</span><span></span></div>
      <div class="row in2"><span>Includes 6g Added Sugars</span><b>12%</b></div>
    </div>
    <p class="note">Lorem ipsum dolor sit amet, consectetuer adipiscing elit, sed diam nonummy nibh euismod</p>
    <div class="label-space"></div>
  </div>
</section>

</body>
</html>
```